Simple elegant business card

General card for a fin and television director.
Just want name, email, phone and address.

Target Market(s)

Prospective employers

Industry/Entity Type

Business

Requirements
Must have
• As above
Nice to have
• Logo but not necessary.
Should not have
• Not too colourful or funky.
• Simplicity and elegance the way to go.

```html
<!DOCTYPE html>
<html lang="en">
<head>
<meta charset="utf-8">
<title>Claire Holloway – Business Card</title>
<link rel="stylesheet" href="https://fonts.googleapis.com/css2?family=Questrial&display=swap">
<style>
  :root {
    --card-centre: #262626;
    --card-mid: #161616;
    --card-edge: #070707;
    --ink: #f4f4f4;
  }
  * { margin: 0; padding: 0; box-sizing: border-box; }
  html, body {
    width: 1200px;
    height: 734px;
    overflow: hidden;
    background: var(--card-edge);
  }
  .card {
    position: relative;
    width: 1200px;
    height: 734px;
    background: radial-gradient(ellipse 75% 75% at 50% 45%, var(--card-centre) 0%, var(--card-mid) 55%, var(--card-edge) 100%);
    font-family: "Questrial", "Century Gothic", sans-serif;
    color: var(--ink);
  }
  .card__name {
    position: absolute;
    top: 322px;
    left: 0;
    width: 100%;
    text-align: center;
    font-size: 46px;
    font-weight: 400;
    letter-spacing: 1.5px;
    line-height: 1;
  }
  .card__contact {
    position: absolute;
    top: 398px;
    left: 0;
    width: 100%;
    text-align: center;
    font-size: 38px;
    letter-spacing: 1.5px;
    line-height: 1;
    white-space: nowrap;
  }
  .card__divider {
    display: inline-block;
    margin: 0 16px 0 22px;
    font-size: 30px;
    vertical-align: 4px;
  }
</style>
</head>
<body>
  <main class="card">
    <h1 class="card__name">CLAIRE HOLLOWAY</h1>
    <p class="card__contact">
      <span class="card__email">claireholloway@mail.com</span><span class="card__divider">•</span><span class="card__phone">+1 310 555 0147</span>
    </p>
  </main>
</body>
</html>
```